Law Firm Business Cards/Letterhead/Envelopes
Holloway Law Firm, PLLC Business Cards/Letterhead/Envelopes
I need double sided standard sized Business Card [3.5" x 2"]
Selective use of Same font as logo and also may use other type of font
Simple
Martin J. Holloway
Attorney & Counselor at Law
2650 Prairie Ridge Road - Suite 1200
Bloomington, MN 55429
martin@holfirm.example
www.holfirm.example
The front of the card I would like to incorporate my logo and firm name, my name, title, address, numbers/fax, email and website. The business card WILL NOT have curved corners. Open to different possibilities but dont want the card too busy....I'd prefer something on the "simple" side...Same goes for envelope and letterhead.
Probably just Logo, Firm name and address all in upper left of envelope.
Letterhead - Logo and firm name up top somewhere...address at bottom....do not include my name and my title on letterhead.
The back of the card I would like to only incorporate the Logo and website OR Logo and firm name and website. The business card WILL NOT have curved corners. Possibly a different color back (possibly grey), but not necessarily. Possibly a watermark of the logo used somewhere...open to different possibilities but dont want the card too busy....I'd prefer something on the "simple" side...
Logo to the Left
Folder Template

```html
<!DOCTYPE html>
<html lang="en">
<head>
<meta charset="utf-8">
<title>Holloway Law Firm, PLLC — Business Card</title>
<link href="https://fonts.googleapis.com/css2?family=Tinos:ital,wght@0,400;0,700;1,400;1,700&display=swap" rel="stylesheet">
<style>
  :root {
    --backdrop: #e9e6e1;
    --card: #ffffff;
    --navy: #1f3f6e;
    --band-dark: #17325c;
    --band-mid: #3d6aa6;
    --band-line: #c9d3e0;
    --ink: #2c2c2c;
    --rule: #9aa3ad;
  }
  * { box-sizing: border-box; margin: 0; padding: 0; }
  html, body {
    width: 1200px; height: 965px; overflow: hidden;
    background: var(--backdrop);
    font-family: "Tinos", "Times New Roman", serif;
  }
  .business-card {
    position: absolute;
    left: 120px; top: 208px;
    width: 960px; height: 549px;
    background: var(--card);
    overflow: hidden;
    box-shadow: 0 6px 18px rgba(0,0,0,.18);
  }
  .edge-band {
    position: absolute; top: 0; bottom: 0; width: 56px;
    background: linear-gradient(90deg, var(--band-dark), var(--band-mid) 55%, var(--band-dark));
  }
  .edge-band--left { left: 0; }
  .edge-band--right { right: 0; }
  .edge-band::after {
    content: ""; position: absolute; top: 0; bottom: 0; width: 3px; background: var(--band-line);
  }
  .edge-band--left::after { right: 6px; }
  .edge-band--right::after { left: 6px; }

  .firm-mark {
    position: absolute; top: 104px; left: 0; right: 0;
    display: flex; justify-content: center; align-items: center; gap: 22px;
  }
  .firm-mark__square { width: 74px; height: 74px; background: var(--navy); }
  .firm-mark__name {
    font-size: 56px; font-weight: 400; color: var(--navy);
    letter-spacing: 1px; line-height: 1;
  }

  .attorney {
    position: absolute; top: 282px; right: 506px;
    text-align: right;
  }
  .attorney__name {
    font-size: 33px; font-weight: 700; color: var(--navy); line-height: 1.15;
  }
  .attorney__title {
    font-size: 25px; font-style: italic; font-weight: 700; color: var(--ink); line-height: 1.2;
  }
  .attorney__address {
    margin-top: 30px;
    font-size: 25px; color: var(--ink); line-height: 1.35;
  }

  .divider {
    position: absolute; left: 484px; top: 286px; width: 2px; height: 196px;
    background: var(--rule);
  }

  .contact-list {
    position: absolute; left: 506px; top: 282px;
    list-style: none;
  }
  .contact-list__item {
    display: flex; align-items: center; gap: 14px;
    font-size: 25px; color: var(--ink); line-height: 40px;
  }
  .contact-list__icon { width: 22px; height: 22px; fill: var(--ink); flex: none; }
</style>
</head>
<body>
  <div class="business-card">
    <div class="edge-band edge-band--left"></div>
    <div class="edge-band edge-band--right"></div>

    <div class="firm-mark">
      <span class="firm-mark__square"></span>
      <span class="firm-mark__name">Holloway Law Firm, PLLC</span>
    </div>

    <div class="attorney">
      <p class="attorney__name">Martin J. Holloway</p>
      <p class="attorney__title">Attorney &amp; Counselor at Law</p>
      <p class="attorney__address">2650 Prairie Ridge Road - Suite 1200<br>Bloomington, MN 55429</p>
    </div>

    <div class="divider"></div>

    <ul class="contact-list">
      <li class="contact-list__item">
        <svg class="contact-list__icon" viewBox="0 0 24 24"><path d="M6.6 10.8a15 15 0 0 0 6.6 6.6l2.2-2.2a1 1 0 0 1 1-.25 11.4 11.4 0 0 0 3.6.6 1 1 0 0 1 1 1V20a1 1 0 0 1-1 1A17 17 0 0 1 3 4a1 1 0 0 1 1-1h3.5a1 1 0 0 1 1 1c0 1.25.2 2.45.6 3.6a1 1 0 0 1-.25 1z"/></svg>
        (T) (888) 555-0142
      </li>
      <li class="contact-list__item">
        <svg class="contact-list__icon" viewBox="0 0 24 24"><path d="M6.6 10.8a15 15 0 0 0 6.6 6.6l2.2-2.2a1 1 0 0 1 1-.25 11.4 11.4 0 0 0 3.6.6 1 1 0 0 1 1 1V20a1 1 0 0 1-1 1A17 17 0 0 1 3 4a1 1 0 0 1 1-1h3.5a1 1 0 0 1 1 1c0 1.25.2 2.45.6 3.6a1 1 0 0 1-.25 1z"/></svg>
        (952) 555-0189
      </li>
      <li class="contact-list__item">
        <svg class="contact-list__icon" viewBox="0 0 24 24"><path d="M6 2h10v6H6zM4 9h16a2 2 0 0 1 2 2v9H2v-9a2 2 0 0 1 2-2zm3 4v2h2v-2zm4 0v2h2v-2zm4 0v2h2v-2zm-8 3v2h2v-2zm4 0v2h2v-2zm4 0v2h2v-2z"/></svg>
        (952) 555-0188
      </li>
      <li class="contact-list__item">
        <svg class="contact-list__icon" viewBox="0 0 24 24"><path d="M12 2a10 10 0 1 0 5 18.7l-1-1.7A8 8 0 1 1 20 12v1a2 2 0 0 1-4 0V7h-2v1a5 5 0 1 0 .6 7.2A4 4 0 0 0 22 13v-1A10 10 0 0 0 12 2zm0 13a3 3 0 1 1 0-6 3 3 0 0 1 0 6z"/></svg>
        martin@holfirm.example
      </li>
      <li class="contact-list__item">
        <svg class="contact-list__icon" viewBox="0 0 24 24"><path d="M12 2a10 10 0 1 0 0 20 10 10 0 0 0 0-20zm6.9 6h-2.8a15 15 0 0 0-1.3-3.9A8 8 0 0 1 18.9 8zM12 4c.8 1.1 1.5 2.5 1.9 4h-3.8c.4-1.5 1.1-2.9 1.9-4zM4.3 14a8 8 0 0 1 0-4h3.3a16 16 0 0 0 0 4zm.8 2h2.8c.3 1.4.8 2.7 1.3 3.9A8 8 0 0 1 5.1 16zm2.8-8H5.1a8 8 0 0 1 4.1-3.9C8.7 5.3 8.2 6.6 7.9 8zM12 20c-.8-1.1-1.5-2.5-1.9-4h3.8c-.4 1.5-1.1 2.9-1.9 4zm2.3-6H9.7a14 14 0 0 1 0-4h4.6a14 14 0 0 1 0 4zm.5 5.9c.5-1.2 1-2.5 1.3-3.9h2.8a8 8 0 0 1-4.1 3.9zm1.6-5.9a16 16 0 0 0 0-4h3.3a8 8 0 0 1 0 4z"/></svg>
        www.holfirm.example
      </li>
    </ul>
  </div>
</body>
</html>
```